Quorvix Letter head

Quorvix is a young and energetic software development consultancy. We spend our time working with clients to turn what ever is in their heads in to software.
We are trying to create an image of a high class software boutique who build class leading bespoke solutions.
We need a sharp letter head that looks great on high quality media.
We like bold colours and distinctive design. So show us what you can do.
Industry/Entity Type
Software
Requirements
Must have
- Our company is based in the UK and are requried to have on the paper somewhere the following information:
* Registered company name: Quorvix Ltd
* Registered company number
* VAT registration number
In addition we also want the following:
* An email address
* Telephone number
* Website address
An example of what some pages have in their footer is something like the following:
Quorvix Ltd is registered in England and Wales. Reg. no: 5316274
Registered office: 48 Cobblewick Road, Harlow Essex, CM93TP. Tel: 07712365081
You do not have to use this sentance but please make sure your design incorporates accommodates the requirements for UK based companies

```html
<!DOCTYPE html>
<html lang="en">
<head>
<meta charset="utf-8">
<title>Quorvix Letterhead</title>
<link href="https://fonts.googleapis.com/css2?family=Questrial&display=swap" rel="stylesheet">
<style>
  :root {
    --backdrop: #a9aab3;
    --paper: #f5f6f8;
    --brand-red: #c8242c;
    --ink-grey: #6e6f75;
    --soft-grey: #9a9ba1;
    --band-grey: #b9bac0;
  }
  * { margin: 0; padding: 0; box-sizing: border-box; }
  html, body {
    width: 1200px;
    height: 1000px;
    overflow: hidden;
    background: var(--backdrop);
    font-family: "Questrial", "Century Gothic", sans-serif;
  }
  .letterhead {
    position: absolute;
    left: 275px;
    top: 40px;
    width: 650px;
    height: 920px;
    background: var(--paper);
    box-shadow: 0 6px 18px rgba(0,0,0,0.18);
  }
  .brand {
    position: absolute;
    left: 52px;
    top: 52px;
    display: flex;
    align-items: center;
    gap: 12px;
  }
  .brand-square {
    width: 22px;
    height: 22px;
    background: var(--brand-red);
  }
  .brand-name {
    font-size: 40px;
    color: var(--ink-grey);
    letter-spacing: 1px;
    line-height: 1;
  }
  .registration {
    position: absolute;
    right: 44px;
    top: 150px;
    text-align: right;
    font-size: 8px;
    line-height: 1.6;
    color: var(--soft-grey);
  }
  .website {
    position: absolute;
    left: 52px;
    bottom: 48px;
    font-size: 11px;
    letter-spacing: 6px;
    color: var(--ink-grey);
  }
  .contact {
    position: absolute;
    left: 330px;
    bottom: 28px;
    font-size: 8px;
    line-height: 1.8;
    color: var(--ink-grey);
  }
  .contact .label { color: var(--brand-red); }
  .contact .gap { display: inline-block; width: 14px; }
  .footer-band {
    position: absolute;
    left: 0;
    bottom: 0;
    width: 100%;
    height: 14px;
    display: flex;
  }
  .footer-band .accent { width: 46%; background: var(--brand-red); }
  .footer-band .rest { flex: 1; background: var(--band-grey); }
</style>
</head>
<body>
  <main class="letterhead">
    <header class="brand">
      <span class="brand-square"></span>
      <span class="brand-name">Quorvix</span>
    </header>

    <p class="registration">
      Quorvix Ltd is registered in England and Wales<br>
      Reg. No: 5316274 - VAT: GB284 6173 90
    </p>

    <p class="website">www.quorvix.com</p>

    <address class="contact">
      48 Cobblewick Road, Harlow Essex, CM93TP<br>
      <span class="label">Phone:</span> 07712365081<span class="gap"></span><span class="label">Email:</span> info@quorvix.com
    </address>

    <div class="footer-band">
      <span class="accent"></span>
      <span class="rest"></span>
    </div>
  </main>
</body>
</html>
```